Tuition Center Website

We need a new web site for a tutoring company based in sydney.

We only teach senior highschool students and pride ourselves on building the students abilities to think their way through life.

I would like a bright and vibrant website that looks professional and modern.
It needs to look simple and neat but also have the functionality we need.
Images and flash would be good.

Please keep in mind that the site must be appealing to a younger audience.

We need a multipage website with the following navigation bars:

1.Home (As logo not "home" button)
I would like a news box/ticker somewhere that can stream our chatterbook and flitter feeds and also any news updates we want to put up.
Subscribe to newsletter button.

2. About us.
This needs to be a pull down into:
-What we do
-Why we do it
-How we do it

3. Courses
Pulldown into:
-Maths
-English
-Science
(we may need to attach extra pages behind these e.g. Courses/Science/Physics or Courses/Science/Chemistry and possibly add a link to a new quizzo form)

4. Inspired
This page is like a blog page where we can upload videos, links to articles that we find to be inspiring and hopefully will inspire others.

5. Inspire
This is a recruitment page. Only content here.

6. Contact us.
Mapzy map widget and a 'contact us' form

* Our branding requires green close to #12FF3D

***Please have a look at the current website.
@ www.brindlelearning.com.au

Thanks everybody hope the revision of my brief is better and more informative than my last one

Target Market(s)

senior highschool students aged 15-19, parents ( to a lesser degree)

Industry/Entity Type

It Company

Requirements
Must have
• Ability to change content on pages.

The green doesn't have to be everywhere, but it must be obvious that it is our colour.

Nice to have
• Sites with a nicer mix of images and flash will be given more consideration. But then again, if you amaze us, you amaze us and we will go with your design.
Should not have
• Should stay away from ocre, brown colours and serif fonts.

```html
<!DOCTYPE html>
<html lang="en">
<head>
<meta charset="utf-8">
<title>Brindle Learning – HSC tutoring &amp; mentoring</title>
<link rel="stylesheet" href="https://fonts.googleapis.com/css2?family=Ubuntu:wght@400;500;700&family=Arimo:ital,wght@0,400;0,700;1,400&display=swap">
<style>
:root{
  --green:#4cb700;
  --green-bright:#62cc00;
  --green-dark:#3a8f00;
  --ink:#333;
  --text:#666;
  --muted:#888;
  --nav:#2e2e2e;
  --footer:#4a4a4a;
  --footer-text:#d0d0d0;
  --line:#e2e2e2;
}
*{box-sizing:border-box;margin:0;padding:0}
html,body{width:990px;height:1200px;overflow:hidden}
body{position:relative;font-family:"Arimo",Arial,sans-serif;color:var(--text);
  background:linear-gradient(#f0f0f0 0,#fbfbfb 100px,#fff 160px,#f7f7f7 475px)}
a{color:inherit;text-decoration:none}
.abs{position:absolute}

/* header */
.util-links{left:107px;top:12px;font-size:9px;color:var(--muted);letter-spacing:.2px}
.util-links span{margin:0 7px;color:#aaa}
.admin-login{left:784px;top:9px;width:99px;height:26px;border-radius:3px;background:var(--green);
  color:#fff;font:700 10px "Arimo",sans-serif;display:flex;align-items:center;justify-content:center;gap:6px}
.admin-login svg{width:13px;height:14px}
.brand{left:107px;top:44px;display:flex;align-items:center;gap:10px}
.brand-square{width:30px;height:30px;background:var(--green);display:block}
.brand-name{font:700 26px/1 "Arimo",sans-serif;color:var(--ink);letter-spacing:-.3px}
.brand-tag{left:148px;top:74px;font:400 10.5px "Arimo",sans-serif;color:var(--muted)}
.header-rule{left:0;top:104px;width:990px;height:2px;background:var(--green-bright)}

.main-nav{left:107px;top:106px;width:776px;height:36px;background:linear-gradient(#3a3a3a,#262626);
  border-radius:0 0 8px 8px;display:flex;align-items:center;padding:0 16px;font-size:10.5px;color:#fff}
.main-nav a{white-space:nowrap}
.main-nav .sep{color:#bbb;margin:0 auto}

/* hero */
.hero{left:107px;top:151px;width:776px;height:270px}
.hero svg{position:absolute;left:0;top:0}
.hero-title{left:27px;top:14px;font:700 43px/1 "Ubuntu",sans-serif;color:var(--green);letter-spacing:.5px}
.hero-sub{left:28px;top:64px;font:500 14px "Ubuntu",sans-serif;color:#222}
.hero-copy{left:28px;top:84px;width:415px;font:500 12px/20px "Ubuntu",sans-serif;color:#555}
.btn-dark{background:linear-gradient(#4a4a4a,#1f1f1f);color:#fff;border:1px solid #111;border-radius:2px;
  box-shadow:0 1px 2px rgba(0,0,0,.4), inset 0 1px 0 rgba(255,255,255,.2);display:flex;align-items:center;justify-content:center}
.hero-cta{left:135px;top:326px;width:139px;height:30px;font:500 15px "Ubuntu",sans-serif}
.hero-shadow{left:280px;top:420px;width:480px;height:14px;border-radius:50%;
  background:radial-gradient(ellipse at center,rgba(0,0,0,.18),rgba(0,0,0,0) 70%)}
.slider-tab{left:430px;top:443px;width:129px;height:33px;background:var(--green-bright);border-radius:8px 8px 0 0;
  display:flex;align-items:center;justify-content:center;gap:7px;padding-bottom:4px}
.slider-tab i{width:16px;height:16px;border-radius:50%;background:#2f7d00;display:block}
.slider-tab i.active{background:#222}

/* content */
.green-band{left:0;top:475px;width:990px;height:555px;background:var(--green)}
.content{left:107px;top:475px;width:776px;height:555px;background:#fff}
.h-green{font:400 18px "Arimo",sans-serif;color:var(--green);white-space:nowrap}
.welcome-title{left:130px;top:491px}
.photo-welcome{left:130px;top:522px;width:347px;height:113px;border:1px solid #ccc;border-radius:4px;
  background:linear-gradient(90deg,#c9a27f,#e9c6a0 30%,#a86f4b 55%,#d7b191 75%,#6f9a5a)}
.welcome-copy{left:130px;top:649px;width:350px;font-size:10.5px;line-height:19px;color:var(--text)}

.blog-box{left:503px;top:494px;width:357px;height:269px;border:1px solid #ddd;border-radius:3px;
  background:linear-gradient(#fff,#f8f8f8);box-shadow:0 3px 0 #ddd}
.blog-head{left:19px;top:14px;display:flex;align-items:center;gap:10px}
.blog-dot{width:20px;height:20px;border-radius:50%;background:#f26522}
.blog-arrows{right:18px;top:18px;display:flex;gap:12px}
.blog-post{left:19px;width:320px;font-size:10.5px;line-height:19px;color:var(--text)}
.blog-post b{color:#333}
.posted{font-style:italic;color:var(--green);margin-top:6px;font-size:10px}
.blog-rule{left:19px;top:144px;width:318px;height:1px;background:var(--line)}

.section-rule{left:130px;top:788px;width:730px;height:1px;background:var(--line)}
.col-rule{top:808px;width:1px;height:172px;background:var(--line)}
.col-title{top:803px}
.quote{left:130px;top:832px;width:210px;font-style:italic;font-size:10.5px;line-height:19px;color:#555}
.quote .mark{font:700 30px/0 "Arimo",sans-serif;color:#bbb;font-style:normal;vertical-align:-10px;margin-right:4px}
.quote-by{left:130px;top:964px;font-size:10.5px;color:#333;font-weight:700}
.quote-by em{color:var(--green);font-weight:400}
.photo-trial{left:382px;top:831px;width:228px;height:74px;border:1px solid #ccc;border-radius:4px;
  background:linear-gradient(90deg,#f1e2d2,#d9a680 25%,#fff 45%,#a0694a 60%,#f0d2b6 80%,#fff)}
.trial-copy{left:386px;top:912px;width:225px;font-size:10.5px;line-height:19px;color:var(--text)}
.trial-cta{left:386px;top:979px;width:117px;height:27px;font:700 11.5px "Arimo",sans-serif}
.news{left:649px;width:215px}
.news h4{font:700 12.5px "Arimo",sans-serif;color:#333;margin-bottom:4px}
.news p{font-size:9.5px;line-height:17px;color:var(--text)}
.news .more{font-style:italic;color:var(--green);font-size:9.5px;margin-top:4px}

/* footer */
.footer{left:0;top:1030px;width:990px;height:170px;background:var(--footer)}
.foot-brand{left:108px;top:1066px;display:flex;align-items:center;gap:8px;font:400 18px "Arimo",sans-serif;color:#bdbdbd}
.foot-brand i{width:26px;height:26px;background:#bdbdbd;display:block}
.foot-copy{left:108px;top:1140px;font-size:9px;line-height:19px;color:#e6e6e6}
.foot-title{font:400 15.5px "Arimo",sans-serif;color:#fff}
.contact{left:516px;top:1053px;font-size:9.5px;line-height:20px;color:var(--footer-text)}
.contact .lbl{color:#fff}
.connect{left:752px;top:1053px}
.social{display:grid;grid-template-columns:auto auto;gap:6px 14px;margin-top:10px;font-size:10.5px;color:#fff}
.social span{display:flex;align-items:center;gap:6px}
.social i{width:10px;height:10px;background:var(--green-bright);display:block}
</style>
</head>
<body>

<header>
  <nav class="abs util-links">
    <a href="#">Board Past Exam Papers</a><span>|</span><a href="#">State Students Online</a><span>|</span><a href="#">Uni Admissions</a><span>|</span><a href="#">Exam Online [Study Resources]</a><span>|</span><a href="#">Help for Study Stress</a>
  </nav>
  <a class="abs admin-login" href="#">
    <svg viewBox="0 0 13 14"><circle cx="6.5" cy="4" r="3.3" fill="#fff"/><path d="M0 14c0-4 3-6 6.5-6S13 10 13 14z" fill="#fff"/></svg>
    Admin Login
  </a>
  <div class="abs brand">
    <i class="brand-square"></i>
    <div class="brand-name">Brindle Learning</div>
  </div>
  <p class="abs brand-tag">HSC tutoring &amp; mentoring for senior students</p>
  <div class="abs header-rule"></div>
  <nav class="abs main-nav">
    <a href="#">Home</a><span class="sep">|</span>
    <a href="#">About Us</a><span class="sep">|</span>
    <a href="#">Find Us</a><span class="sep">|</span>
    <a href="#">Get in Touch</a><span class="sep">|</span>
    <a href="#">Recent News</a><span class="sep">|</span>
    <a href="#">Year 10 Classes</a><span class="sep">|</span>
    <a href="#">Yr 11 &amp; 12 HSC Classes</a>
  </nav>
</header>

<section class="abs hero">
  <svg width="776" height="270" viewBox="0 0 776 270">
    <defs>
      <clipPath id="heroClip">
        <path d="M8,4 H768 Q772,4 772,8 V203 Q772,226 738,238 Q560,264 390,262 Q120,258 32,231 Q4,222 4,203 V8 Q4,4 8,4 Z"/>
      </clipPath>
      <linearGradient id="heroPhoto" x1="0" x2="1" y1="0" y2="0">
        <stop offset="0" stop-color="#ffffff"/>
        <stop offset=".18" stop-color="#eef0ec"/>
        <stop offset=".45" stop-color="#d9b48c"/>
        <stop offset=".7" stop-color="#c89a70"/>
        <stop offset="1" stop-color="#4f7a48"/>
      </linearGradient>
    </defs>
    <path d="M6,0 H770 Q776,0 776,6 V205 Q776,230 740,243 Q560,270 390,266 Q120,262 30,235 Q0,225 0,205 V6 Q0,0 6,0 Z" fill="#fff" stroke="#d8d8d8"/>
    <rect x="355" y="4" width="421" height="266" fill="url(#heroPhoto)" clip-path="url(#heroClip)" role="img" aria-label="Photo of a smiling senior student"/>
  </svg>
  <h1 class="abs hero-title">i am brindle.</h1>
  <p class="abs hero-sub">real HSC coaching &amp; mentoring.</p>
  <p class="abs hero-copy">The HSC help you need, in the years you need it. We offer small classes, individualised attention and genuine care for each student. It's different in a good way. Feel free to find out more about us, and let us know if there's any way we can help you on your journey.</p>
</section>
<a class="abs btn-dark hero-cta" href="#">Enquire Now</a>
<div class="abs hero-shadow"></div>

<div class="abs green-band"></div>
<div class="abs slider-tab"><i class="active"></i><i></i><i></i><i></i></div>
<main class="abs content"></main>

<h2 class="abs h-green welcome-title">Welcome to Our Site</h2>
<div class="abs photo-welcome" role="img" aria-label="Group photo of smiling high school students"></div>
<p class="abs welcome-copy">Aliquam molestie, mi et imperdiet euismod, dui purus auctor tellus, et interdum lacus lectus et ante. Sed accumsan sollicitudin sapien, sit amet adipiscing turpis gravida ac. In congue, neque ac lobortis volut­pat, libero mauris varius mi, vitae suscipit ipsum ligula vitae risus. Duis aliquam nibh a dui iaculis viverra id a velit. Vivamus egestas risus in magna varius commodo.</p>

<aside class="abs blog-box">
  <div class="abs blog-head"><span class="blog-dot"></span><h3 class="h-green">Recent Blog Post</h3></div>
  <div class="abs blog-arrows">
    <svg width="10" height="16" viewBox="0 0 10 16"><path d="M8 2 2 8l6 6" fill="none" stroke="#555" stroke-width="2"/></svg>
    <svg width="10" height="16" viewBox="0 0 10 16"><path d="m2 2 6 6-6 6" fill="none" stroke="#555" stroke-width="2"/></svg>
  </div>
  <article class="abs blog-post" style="top:56px">
    <p><b>Aliquam molestie, mi et imperdiet euismod,</b> dui purus auctor tellus, et interdum lacus lectus et ante. Sed accumsan sollicitudin sapien, sit amet adipiscing turpis gravida ac.</p>
    <p class="posted">Posted on March 29, 2013</p>
  </article>
  <div class="abs blog-rule"></div>
  <article class="abs blog-post" style="top:162px">
    <p><b>Aliquam molestie, mi et imperdiet euismod,</b> dui purus auctor tellus, et interdum lacus lectus et ante. Sed accumsan sollicitudin sapien, sit amet adipiscing turpis gravida ac.</p>
    <p class="posted">Posted on March 29, 2013</p>
  </article>
</aside>

<div class="abs section-rule"></div>
<div class="abs col-rule" style="left:363px"></div>
<div class="abs col-rule" style="left:629px"></div>

<h3 class="abs h-green col-title" style="left:130px">What Our Students Say.</h3>
<blockquote class="abs quote"><span class="mark">“</span>Brindle is character-building, motivating and more than just a tuition centre. (They) discipline you to study, but it's flexible and enjoyable. They really help you achieve more than you thought you ever could...... <span class="mark">”</span></blockquote>
<p class="abs quote-by">~Marcus, <em>Northvale Boys HS</em></p>

<h3 class="abs h-green col-title" style="left:383px">Ask for your Free Trial Lesson</h3>
<div class="abs photo-trial" role="img" aria-label="Photo of many raised hands"></div>
<p class="abs trial-copy">Because we believe you shouldn't have to sign up until you see what it's actually like. Call or email us now!</p>
<a class="abs btn-dark trial-cta" href="#">Send an Enquiry</a>

<h3 class="abs h-green col-title" style="left:649px">Recent News</h3>
<div class="abs news" style="top:837px">
  <h4>Year 11 FREE HSC Workshops!</h4>
  <p>This is a great opportunity to get prepared for your HSC year.</p>
  <p class="more">Read More</p>
</div>
<div class="abs news" style="top:924px">
  <h4>Uni Open Days 2012</h4>
  <p>Many students are thrown into near-despair over their university preferences.</p>
  <p class="more">Read More</p>
</div>

<footer class="abs footer"></footer>
<div class="abs foot-brand"><i></i>brindle</div>
<p class="abs foot-copy">© 2013 Brindle Learning | HSC tutoring &amp; mentoring<br>All Right Reserved</p>
<div class="abs contact">
  <h3 class="foot-title">Contact Us</h3>
  <p>Street: 48 Larkfield</p>
  <p>Rd Larkfield NSW 2190</p>
  <p class="lbl">Phone:</p>
  <p>(02) 5550 1234</p>
  <p class="lbl">Email:</p>
  <p>learn@brindlelearning.com.au</p>
</div>
<div class="abs connect">
  <h3 class="foot-title">Connect Us on</h3>
  <div class="social">
    <span><i></i>chatterbook</span><span><i></i>flitter</span>
    <span><i></i>linkup</span><span><i></i>feed</span>
  </div>
</div>

</body>
</html>
```